Staffing Firm - Business Cards and Stationary
Business Cards, Letterhead, Envelopes and Brochure Layout
I need double sided standard sized Business Card [3.5" x 2"]
Use whatever fonts that you think are best.
Professional
Todd Dunlap
President/CEO
2250 North Birch Avenue, Ste 730
Dalwick, TX 75590
Direct Line - 832-555-0143
tdunlap@kelvor.com
www.kelvor.com
We would like them to be memorable but professional.
Possibly put the various divisions?
We will need layouts for each group/division.

```html
<!DOCTYPE html>
<html lang="en">
<head>
<meta charset="utf-8">
<title>Kelvor Staffing – Stationery Set</title>
<link rel="stylesheet" href="https://fonts.googleapis.com/css2?family=Cinzel:wght@500&family=Open+Sans:wght@400;600&display=swap">
<style>
  :root {
    --bg: #e9e7e4;
    --paper: #ffffff;
    --ink: #333333;
    --ink-soft: #6b6b6b;
    --rule: #b9b9b9;
    --black-1: #2b2b2b;
    --black-2: #0d0d0d;
    --logo-light: #e8e8e8;
    --audit: #7a1f2b;
    --executive: #4b2a6b;
    --finance: #b3322a;
    --systems: #2d4f8a;
    --general: #4a6b3a;
  }
  * { box-sizing: border-box; margin: 0; padding: 0; }
  html, body { width: 1200px; height: 850px; overflow: hidden; }
  body {
    position: relative;
    background: var(--bg);
    font-family: "Open Sans", Arial, sans-serif;
    color: var(--ink);
  }
  .wordmark {
    font-family: "Cinzel", "Times New Roman", serif;
    font-weight: 500;
    letter-spacing: 0.06em;
    color: var(--ink);
    white-space: nowrap;
  }
  .wordmark--light { color: var(--logo-light); }

  /* Business cards */
  .card {
    position: absolute;
    width: 154px; height: 86px;
    box-shadow: 0 1px 3px rgba(0,0,0,.25);
  }
  .card--front { left: 86px; background: var(--paper); padding: 8px 9px; }
  .card--back {
    left: 250px;
    background: linear-gradient(135deg, var(--black-1), var(--black-2));
    display: flex; align-items: center; justify-content: center;
  }
  .card--back .wordmark { font-size: 12px; }
  .card__logo { font-size: 7px; }
  .card__person { position: absolute; left: 9px; top: 36px; font-size: 5px; line-height: 1.4; white-space: nowrap; }
  .card__name { font-weight: 600; font-size: 5.5px; }
  .card__details {
    position: absolute; left: 66px; top: 20px;
    font-size: 4.2px; line-height: 1.5; color: var(--ink-soft);
    border-left: 0.5px solid var(--rule); padding-left: 4px;
    white-space: nowrap;
  }
  .card__stripe { position: absolute; left: 0; right: 0; bottom: 0; height: 3px; }
  .row-1 { top: 34px; } .row-2 { top: 144px; } .row-3 { top: 254px; }
  .row-4 { top: 365px; } .row-5 { top: 475px; }

  /* Letterhead */
  .letterhead {
    position: absolute; left: 499px; top: 19px;
    width: 504px; height: 578px;
    background: var(--paper);
    box-shadow: 0 2px 5px rgba(0,0,0,.25);
  }
  .letterhead .wordmark { position: absolute; left: 28px; top: 26px; font-size: 18px; }
  .contact-block {
    position: absolute; left: 262px; top: 22px;
    border-left: 1px solid var(--rule); padding-left: 10px;
    font-size: 7px; line-height: 1.55; color: var(--ink-soft);
    white-space: nowrap;
  }
  .contact-block dl { display: grid; grid-template-columns: 30px auto; margin-top: 4px; }
  .divisions {
    position: absolute; left: 24px; right: 24px; bottom: 18px;
    display: flex; justify-content: space-between;
    font-size: 6.5px; font-weight: 600;
    white-space: nowrap;
  }
  .division { padding-top: 3px; border-top: 1.5px solid currentColor; }
  .division--audit { color: var(--audit); }
  .division--executive { color: var(--executive); }
  .division--finance { color: var(--finance); }
  .division--systems { color: var(--systems); }

  /* Envelopes */
  .envelope-front {
    position: absolute; left: 43px; top: 619px;
    width: 480px; height: 186px;
    background: var(--paper);
    box-shadow: 0 2px 5px rgba(0,0,0,.25);
  }
  .envelope-front .wordmark { position: absolute; left: 20px; top: 20px; font-size: 16px; }
  .envelope-front .contact-block { left: 224px; top: 18px; }
  .envelope-front .divisions { bottom: 14px; left: 20px; right: 20px; }
  .envelope-back {
    position: absolute; left: 557px; top: 619px;
    width: 518px; height: 192px;
    box-shadow: 0 2px 5px rgba(0,0,0,.25);
  }
  .envelope-back svg { position: absolute; inset: 0; }
  .envelope-back .wordmark {
    position: absolute; left: 0; right: 0; top: 40px;
    text-align: center; font-size: 17px;
  }
</style>
</head>
<body>

  <!-- Business card fronts -->
  <article class="card card--front row-1">
    <div class="card__logo wordmark">Kelvor Staffing</div>
    <div class="card__person"><div class="card__name">Todd Dunlap</div><div>President/CEO</div></div>
    <div class="card__details">
      <div>2250 North Birch Avenue, Ste 730</div><div>Dalwick, TX 75590</div>
      <div>Direct: 832-555-0143</div><div>tdunlap@kelvor.com</div><div>www.kelvor.com</div>
    </div>
    <div class="card__stripe" style="background: var(--general)"></div>
  </article>
  <article class="card card--front row-2">
    <div class="card__logo wordmark">Kelvor Staffing</div>
    <div class="card__person"><div class="card__name">Todd Dunlap</div><div>President/CEO</div></div>
    <div class="card__details">
      <div>2250 North Birch Avenue, Ste 730</div><div>Dalwick, TX 75590</div>
      <div>Direct: 832-555-0143</div><div>tdunlap@kelvor.com</div><div>www.kelvor.com</div>
    </div>
    <div class="card__stripe" style="background: var(--audit)"></div>
  </article>
  <article class="card card--front row-3">
    <div class="card__logo wordmark">Kelvor Staffing</div>
    <div class="card__person"><div class="card__name">Todd Dunlap</div><div>President/CEO</div></div>
    <div class="card__details">
      <div>2250 North Birch Avenue, Ste 730</div><div>Dalwick, TX 75590</div>
      <div>Direct: 832-555-0143</div><div>tdunlap@kelvor.com</div><div>www.kelvor.com</div>
    </div>
    <div class="card__stripe" style="background: var(--executive)"></div>
  </article>
  <article class="card card--front row-4">
    <div class="card__logo wordmark">Kelvor Staffing</div>
    <div class="card__person"><div class="card__name">Todd Dunlap</div><div>President/CEO</div></div>
    <div class="card__details">
      <div>2250 North Birch Avenue, Ste 730</div><div>Dalwick, TX 75590</div>
      <div>Direct: 832-555-0143</div><div>tdunlap@kelvor.com</div><div>www.kelvor.com</div>
    </div>
    <div class="card__stripe" style="background: var(--finance)"></div>
  </article>
  <article class="card card--front row-5">
    <div class="card__logo wordmark">Kelvor Staffing</div>
    <div class="card__person"><div class="card__name">Todd Dunlap</div><div>President/CEO</div></div>
    <div class="card__details">
      <div>2250 North Birch Avenue, Ste 730</div><div>Dalwick, TX 75590</div>
      <div>Direct: 832-555-0143</div><div>tdunlap@kelvor.com</div><div>www.kelvor.com</div>
    </div>
    <div class="card__stripe" style="background: var(--systems)"></div>
  </article>

  <!-- Business card backs -->
  <article class="card card--back row-1"><span class="wordmark wordmark--light">Kelvor Staffing</span></article>
  <article class="card card--back row-2"><span class="wordmark wordmark--light">Kelvor Staffing</span></article>
  <article class="card card--back row-3"><span class="wordmark wordmark--light">Kelvor Staffing</span></article>
  <article class="card card--back row-4"><span class="wordmark wordmark--light">Kelvor Staffing</span></article>
  <article class="card card--back row-5"><span class="wordmark wordmark--light">Kelvor Staffing</span></article>

  <!-- Letterhead -->
  <section class="letterhead">
    <div class="wordmark">Kelvor Staffing</div>
    <div class="contact-block">
      <div>2250 North Birch Avenue, Ste 730</div>
      <div>Dalwick, TX 75590</div>
      <dl>
        <dt>Phone</dt><dd>832-555-0143</dd>
        <dt>Fax</dt><dd>832-555-0198</dd>
        <dt>Email</dt><dd>tdunlap@kelvor.com</dd>
        <dt>Web</dt><dd>www.kelvor.com</dd>
      </dl>
    </div>
    <footer class="divisions">
      <span class="division division--audit">audit and compliance group</span>
      <span class="division division--executive">executive placement group</span>
      <span class="division division--finance">finance staffing group</span>
      <span class="division division--systems">systems staffing group</span>
    </footer>
  </section>

  <!-- Envelope front -->
  <section class="envelope-front">
    <div class="wordmark">Kelvor Staffing</div>
    <div class="contact-block">
      <div>2250 North Birch Avenue, Ste 730</div>
      <div>Dalwick, TX 75590</div>
    </div>
    <footer class="divisions">
      <span class="division division--audit">audit and compliance group</span>
      <span class="division division--executive">executive placement group</span>
      <span class="division division--finance">finance staffing group</span>
      <span class="division division--systems">systems staffing group</span>
    </footer>
  </section>

  <!-- Envelope back -->
  <section class="envelope-back">
    <svg width="518" height="192" viewBox="0 0 518 192">
      <defs>
        <linearGradient id="flap" x1="0" y1="0" x2="0" y2="1">
          <stop offset="0" stop-color="#2b2b2b"/>
          <stop offset="1" stop-color="#0d0d0d"/>
        </linearGradient>
      </defs>
      <rect width="518" height="192" fill="#ffffff"/>
      <line x1="0" y1="192" x2="259" y2="112" stroke="#dddddd" stroke-width="1"/>
      <line x1="518" y1="192" x2="259" y2="112" stroke="#dddddd" stroke-width="1"/>
      <polygon points="0,0 518,0 259,118" fill="url(#flap)"/>
    </svg>
    <div class="wordmark wordmark--light">Kelvor Staffing</div>
  </section>

</body>
</html>
```